Australian Web Design company needs a business card design

We need a business card design for a Sydney based Web Design/Development company called "Tall Pine Web Design". We design, build and deploy websites for small to medium sized businesses. The final design should be clean and communicate that we are a professional and supportive company.
I'd like the Icon to be abstract. Something that embodies the power of the internet, needs to be clean/professional and show that we are human and that we support our customers. Hope that helps.
Target Market(s)
All small to medium businesses
Industry/Entity Type
Business
Contact Information for Business Card
Martin Forbes
Tall Pine Web Design
17 Wattle Grove Road
West Kelsworth
NSW 2250
0438 527 064
martin@tallpinewebdesign.com.au
www.tallpinewebdesign.com.au

```html
<!DOCTYPE html>
<html lang="en">
<head>
<meta charset="utf-8">
<title>Tall Pine Web Design – Business Card</title>
<link rel="stylesheet" href="https://fonts.googleapis.com/css2?family=Arimo:wght@400&display=swap">
<style>
  :root {
    --backdrop: #6e4528;
    --card: #3d4047;
    --chrome: #d6d6d6;
    --chrome-edge: #b9b9b9;
    --field: #f4f4f4;
    --field-text: #444;
    --light: #e4e4e6;
    --muted: #b9bbc0;
    --white: #ffffff;
    --icon-ink: #3d4047;
    --dot-red: #ee5b55;
    --dot-amber: #e0b23a;
    --dot-green: #6cbf4a;
  }
  * { box-sizing: border-box; margin: 0; padding: 0; }
  html, body { width: 1200px; height: 440px; overflow: hidden; }
  body {
    position: relative;
    background: var(--backdrop);
    font-family: "Arimo", Arial, sans-serif;
  }
  .card {
    position: absolute;
    top: 53px;
    width: 554px;
    height: 324px;
    background: var(--card);
    border-radius: 4px 4px 0 0;
    overflow: hidden;
    box-shadow: 0 4px 14px rgba(0,0,0,.45);
  }
  .card--front { left: 37px; }
  .card--back { left: 604px; }

  .toolbar {
    position: relative;
    height: 40px;
    background: linear-gradient(#e2e2e2, var(--chrome));
    border-bottom: 1px solid var(--chrome-edge);
  }
  .toolbar__dots { position: absolute; left: 7px; top: 4px; display: flex; gap: 5px; }
  .toolbar__dot { width: 8px; height: 8px; border-radius: 50%; }
  .toolbar__dot--close { background: var(--dot-red); }
  .toolbar__dot--min { background: var(--dot-amber); }
  .toolbar__dot--max { background: var(--dot-green); }
  .toolbar__expand { position: absolute; right: 6px; top: 4px; }
  .toolbar__nav { position: absolute; left: 10px; top: 20px; font-size: 8px; color: #888; letter-spacing: 4px; }
  .toolbar__address {
    position: absolute; left: 45px; top: 16px; width: 286px; height: 15px;
    background: var(--field); border: 1px solid #c4c4c4; border-radius: 8px;
    font-size: 11px; line-height: 13px; color: var(--field-text); padding-left: 19px;
  }
  .toolbar__address::before { content: "+"; position: absolute; left: 6px; top: 0; color: #aaa; }
  .toolbar__reload { position: absolute; right: 6px; top: 2px; }
  .toolbar__search {
    position: absolute; left: 336px; top: 16px; width: 187px; height: 15px;
    background: var(--field); border: 1px solid #c4c4c4; border-radius: 8px;
  }
  .toolbar__search svg { position: absolute; left: 6px; top: 2px; }
  .toolbar__menu {
    position: absolute; left: 532px; top: 17px; width: 13px; height: 13px;
    border-radius: 50%; background: #e8e8e8; border: 1px solid #c4c4c4;
  }

  .identity {
    position: absolute; left: 0; right: 0; top: 40px; bottom: 0;
    display: flex; flex-direction: column; align-items: center; justify-content: center;
    padding-bottom: 20px;
  }
  .identity__name {
    font-size: 40px; font-weight: 400; color: var(--light);
    white-space: nowrap;
  }
  .identity__person {
    margin-top: 14px; font-size: 13px; color: var(--muted); white-space: nowrap;
  }

  .contact {
    position: absolute; top: 116px;
    display: flex; flex-direction: column; align-items: center;
    transform: translateX(-50%);
  }
  .contact--email { left: 97px; }
  .contact--address { left: 286px; }
  .contact--web { left: 467px; }
  .contact__icon {
    width: 72px; height: 72px; border-radius: 50%;
    background: var(--white);
    display: flex; align-items: center; justify-content: center;
    margin-bottom: 17px;
  }
  .contact__www { font-size: 15px; color: var(--icon-ink); letter-spacing: 1px; }
  .contact__text { color: var(--white); font-size: 11px; line-height: 14px; text-align: center; white-space: nowrap; }

  .social-bar {
    position: absolute; left: 166px; top: 279px; width: 217px; height: 20px;
    background: var(--white); border-radius: 10px;
    display: flex; align-items: center; justify-content: space-between; padding: 0 9px;
    color: var(--icon-ink); font-size: 12px;
  }
  .social-bar__group { display: flex; gap: 7px; }
  .social-bar__spot { width: 11px; height: 11px; border-radius: 50%; background: var(--icon-ink); }
</style>
</head>
<body>

<section class="card card--front">
  <div class="toolbar">
    <div class="toolbar__dots"><span class="toolbar__dot toolbar__dot--close"></span><span class="toolbar__dot toolbar__dot--min"></span><span class="toolbar__dot toolbar__dot--max"></span></div>
    <svg class="toolbar__expand" width="10" height="10" viewBox="0 0 10 10" aria-hidden="true"><path d="M6 1h3v3M4 9H1V6M9 1 6 4M1 9l3-3" fill="none" stroke="#999" stroke-width="1.2"/></svg>
    <div class="toolbar__nav">◀▶</div>
    <div class="toolbar__address">www.tallpinewebdesign.com.au
      <svg class="toolbar__reload" width="9" height="9" viewBox="0 0 10 10" aria-hidden="true"><path d="M8.5 5A3.5 3.5 0 1 1 7 2.2M7 0.5v2h-2" fill="none" stroke="#999" stroke-width="1.2"/></svg>
    </div>
    <div class="toolbar__search"><svg width="9" height="9" viewBox="0 0 10 10" aria-hidden="true"><circle cx="4" cy="4" r="3" fill="none" stroke="#aaa" stroke-width="1.2"/><path d="M6.3 6.3 9 9" stroke="#aaa" stroke-width="1.2"/></svg></div>
    <div class="toolbar__menu"></div>
  </div>
  <div class="identity">
    <h1 class="identity__name">Tall Pine Web Design</h1>
    <p class="identity__person">Martin Forbes · 0438 527 064</p>
  </div>
</section>

<section class="card card--back">
  <div class="toolbar">
    <div class="toolbar__dots"><span class="toolbar__dot toolbar__dot--close"></span><span class="toolbar__dot toolbar__dot--min"></span><span class="toolbar__dot toolbar__dot--max"></span></div>
    <svg class="toolbar__expand" width="10" height="10" viewBox="0 0 10 10" aria-hidden="true"><path d="M6 1h3v3M4 9H1V6M9 1 6 4M1 9l3-3" fill="none" stroke="#999" stroke-width="1.2"/></svg>
    <div class="toolbar__nav">◀▶</div>
    <div class="toolbar__address">www.tallpinewebdesign.com.au
      <svg class="toolbar__reload" width="9" height="9" viewBox="0 0 10 10" aria-hidden="true"><path d="M8.5 5A3.5 3.5 0 1 1 7 2.2M7 0.5v2h-2" fill="none" stroke="#999" stroke-width="1.2"/></svg>
    </div>
    <div class="toolbar__search"><svg width="9" height="9" viewBox="0 0 10 10" aria-hidden="true"><circle cx="4" cy="4" r="3" fill="none" stroke="#aaa" stroke-width="1.2"/><path d="M6.3 6.3 9 9" stroke="#aaa" stroke-width="1.2"/></svg></div>
    <div class="toolbar__menu"></div>
  </div>

  <div class="contact contact--email">
    <div class="contact__icon">
      <svg width="44" height="32" viewBox="0 0 44 32" aria-hidden="true">
        <rect x="2" y="2" width="40" height="28" fill="none" stroke="var(--icon-ink)" stroke-width="2.5"/>
        <path d="M2 2 L22 19 L42 2 M2 30 L17 15 M42 30 L27 15" fill="none" stroke="var(--icon-ink)" stroke-width="2.5"/>
      </svg>
    </div>
    <p class="contact__text">martin@tallpinewebdesign.com.au</p>
  </div>
  <div class="contact contact--address">
    <div class="contact__icon">
      <svg width="26" height="40" viewBox="0 0 26 40" aria-hidden="true">
        <path d="M13 0 C5.8 0 0 5.8 0 13 C0 22 13 40 13 40 C13 40 26 22 26 13 C26 5.8 20.2 0 13 0 Z" fill="var(--icon-ink)"/>
        <circle cx="13" cy="13" r="5" fill="var(--white)"/>
      </svg>
    </div>
    <p class="contact__text">17 Wattle Grove Road West Kelsworth</p>
  </div>
  <div class="contact contact--web">
    <div class="contact__icon"><span class="contact__www">www</span></div>
    <p class="contact__text">www.tallpinewebdesign.com.au</p>
  </div>

  <div class="social-bar">
    <div class="social-bar__group"><span class="social-bar__spot"></span><span class="social-bar__spot"></span></div>
    <span class="social-bar__tag">#tallpine</span>
    <div class="social-bar__group"><span class="social-bar__spot"></span><span class="social-bar__spot"></span></div>
  </div>
</section>

</body>
</html>
```